Ferncrest Dental, LLC business card project

Business card to be designed with current logo.
Dental office- please keep design of card that looks clean and professional.
Please include the following info:
Ferncrest Dental, LLC
Dr. Lorna Pettigrew
2871 Marlowe Street
Bethlehem, PA 18093
610-555-0193
ferncrestdental.office@examplemail.test
Hello everyone-
Reason: Just got back from overseas- will look at all designs and provide feedback. Thank you!
Reason: Polling my friends for the final selection-
thank you to all those that participated- so many talented designers!

```html
<!DOCTYPE html>
<html lang="en">
<head>
<meta charset="utf-8">
<title>Ferncrest Dental – Business Card</title>
<link rel="stylesheet" href="https://fonts.googleapis.com/css2?family=Saira:wght@500;600&family=Questrial&display=swap">
<style>
  :root {
    --page: #ffffff;
    --stone-dark: #1c1c1c;
    --stone-mid: #2e2e2e;
    --stone-light: #3a3a3a;
    --ink-light: #e4e8ea;
    --logo-panel: #ffffff;
    --logo-green: #7cc243;
  }
  * { margin: 0; padding: 0; box-sizing: border-box; }
  html, body {
    width: 1200px;
    height: 1000px;
    overflow: hidden;
    background: var(--page);
  }
  .canvas {
    position: relative;
    width: 1200px;
    height: 1000px;
  }
  .card {
    position: absolute;
    left: 57px;
    top: 181px;
    width: 1088px;
    height: 637px;
    overflow: hidden;
  }
  .card__texture {
    position: absolute;
    inset: 0;
    background:
      radial-gradient(ellipse at 30% 40%, var(--stone-light) 0%, transparent 60%),
      radial-gradient(ellipse at 80% 70%, var(--stone-mid) 0%, transparent 55%),
      linear-gradient(160deg, var(--stone-mid) 0%, var(--stone-dark) 55%, #151515 100%);
  }
  .logo-panel {
    position: absolute;
    left: 50px;
    top: 46px;
    width: 703px;
    height: 123px;
    background: var(--logo-panel);
    display: flex;
    align-items: center;
    padding-left: 48px;
    gap: 22px;
  }
  .logo-panel__dot {
    width: 44px;
    height: 44px;
    border-radius: 50%;
    background: var(--logo-green);
    flex: none;
  }
  .logo-panel__name {
    font-family: "Saira", sans-serif;
    font-weight: 500;
    font-size: 64px;
    color: var(--logo-green);
    line-height: 1;
  }
  .contact {
    position: absolute;
    color: var(--ink-light);
  }
  .contact__doctor {
    left: 48px;
    top: 200px;
    font-family: "Saira", sans-serif;
    font-weight: 600;
    font-size: 62px;
    line-height: 1;
    letter-spacing: -0.5px;
  }
  .contact__address {
    left: 50px;
    top: 290px;
    font-family: "Saira", sans-serif;
    font-weight: 600;
    font-size: 44px;
    line-height: 70px;
    font-style: normal;
  }
  .contact__details {
    right: 47px;
    top: 362px;
    text-align: right;
  }
  .contact__label {
    font-family: "Saira", sans-serif;
    font-weight: 600;
    font-size: 38px;
    font-variant: small-caps;
    letter-spacing: 4px;
    line-height: 1;
  }
  .contact__phone {
    font-family: "Saira", sans-serif;
    font-weight: 600;
    font-size: 50px;
    line-height: 1;
    margin: 18px 0 22px;
    letter-spacing: 1px;
  }
  .contact__email {
    font-family: "Questrial", sans-serif;
    font-size: 42px;
    line-height: 1;
    margin-top: 20px;
    letter-spacing: 0.3px;
  }
</style>
</head>
<body>
<div class="canvas">
  <section class="card">
    <div class="card__texture" role="img" aria-label="Dark grey marble stone texture background"></div>

    <div class="logo-panel">
      <span class="logo-panel__dot"></span>
      <span class="logo-panel__name">Ferncrest Dental</span>
    </div>

    <h1 class="contact contact__doctor">Dr. Lorna Pettigrew</h1>

    <address class="contact contact__address">
      2871 Marlowe Street,<br>
      Bethlehem,<br>
      PA&nbsp; 18093
    </address>

    <div class="contact contact__details">
      <div class="contact__label">Phone:</div>
      <div class="contact__phone">610–555–0193</div>
      <div class="contact__label">E-mail:</div>
      <div class="contact__email">ferncrestdental.office@examplemail.test</div>
    </div>
  </section>
</div>
</body>
</html>
```